TVM8 Business Card Design Project

Design which catches the client with the first impression. A design which is professional and classy with elegance. We have also got another project running and the winning prize for that is $240 "tvm8 print + graphic design".
For all the company details please visit www.tvm8.com.
Please find the logo attached and i would like to have good colors for my business card.
, Design which catches the client with the first impression. A design which is professional and classy with elegance.
TVM8 is running two projects at the same time, please feel free to participate. The other project name is
Business

```html
<!DOCTYPE html>
<html lang="en">
<head>
<meta charset="utf-8">
<title>TVM8 Business Card</title>
<link rel="stylesheet" href="https://fonts.googleapis.com/css2?family=Open+Sans:wght@400;600;700&display=swap">
<style>
  :root {
    --stage: #2a2e2f;
    --lime: #a2cc3a;
    --teal: #3db383;
    --teal-text: #38a878;
    --ink: #555a5c;
    --ink-strong: #3f4446;
    --paper: #ffffff;
  }
  * { box-sizing: border-box; margin: 0; padding: 0; }
  html, body {
    width: 1200px; height: 748px; overflow: hidden;
    background: var(--stage);
    font-family: "Open Sans", Arial, sans-serif;
  }
  .stage {
    position: relative; width: 1200px; height: 748px;
    display: flex; align-items: center; justify-content: center; gap: 40px;
  }
  .card {
    position: relative; width: 520px; height: 296px; overflow: hidden;
    box-shadow: 0 6px 18px rgba(0,0,0,.35);
  }

  /* Front */
  .card--front {
    background: var(--lime);
    display: flex; flex-direction: column; align-items: center; justify-content: center;
    color: var(--paper);
  }
  .brand {
    display: flex; align-items: center; gap: 10px;
    font-weight: 700; letter-spacing: 1px;
  }
  .brand__dot { border-radius: 50%; flex: none; }
  .card--front .brand { font-size: 40px; }
  .card--front .brand__dot { width: 18px; height: 18px; background: var(--paper); }
  .front__company { margin-top: 4px; font-size: 15px; }

  /* Back */
  .card--back { background: var(--paper); }
  .contact {
    position: absolute; left: 62px; top: 118px;
    color: var(--ink); font-size: 10.5px; line-height: 13px;
  }
  .contact__company {
    color: var(--teal-text); font-size: 17px; line-height: 22px; margin-bottom: 12px;
  }
  .contact__lines { margin-bottom: 12px; }
  .contact__label { font-weight: 700; color: var(--ink-strong); margin-right: 4px; }

  .card--back .brand {
    position: absolute; left: 282px; top: 42px;
    font-size: 36px; color: var(--teal-text);
  }
  .card--back .brand__dot { width: 16px; height: 16px; background: var(--lime); }

  .services {
    position: absolute; left: 322px; top: 100px; list-style: none;
    color: var(--ink-strong); font-size: 12.5px; font-weight: 600; line-height: 21px;
  }
  .services li { display: flex; align-items: center; gap: 9px; }
  .services li::before {
    content: ""; width: 7px; height: 7px; border-radius: 50%; background: var(--teal);
  }

  .footer-band {
    position: absolute; left: 0; right: 0; bottom: 0; height: 34px; display: flex;
  }
  .footer-band__lime { flex: 0 0 58%; background: var(--lime); }
  .footer-band__teal { flex: 1; background: var(--teal); }
  .footer-band__dot {
    position: absolute; left: 58%; top: 50%; width: 12px; height: 12px;
    margin: -6px 0 0 -6px; border-radius: 50%; background: var(--paper);
  }
</style>
</head>
<body>
  <main class="stage">
    <section class="card card--front" aria-label="Business card front">
      <div class="brand"><span class="brand__dot"></span><span class="brand__name">TVM8</span></div>
      <p class="front__company">TVM8 Pty Ltd</p>
    </section>

    <section class="card card--back" aria-label="Business card back">
      <div class="brand"><span class="brand__dot"></span><span class="brand__name">TVM8</span></div>

      <ul class="services">
        <li>Information Technology</li>
        <li>Food Services</li>
        <li>Lighting</li>
        <li>Child Care Centres</li>
        <li>Extreme Sports</li>
      </ul>

      <address class="contact" style="font-style:normal">
        <p class="contact__company">TVM8 Pty Ltd</p>
        <p class="contact__lines">
          118 Larkfield Row 03<br>
          7th Street Dunmore<br>
          Westbrook<br>
          Halden<br>
          307415
        </p>
        <p><span class="contact__label">T:</span>362.718.2094</p>
        <p><span class="contact__label">W:</span>www.tvm8.com</p>
      </address>

      <div class="footer-band">
        <span class="footer-band__lime"></span>
        <span class="footer-band__teal"></span>
        <span class="footer-band__dot"></span>
      </div>
    </section>
  </main>
</body>
</html>
```